Letterhead and Envelope Design for Investment Company

We need a letterhead and envelope design.
We are a family owned investment company doing direct investments into other family owned businesses.
I have attached all our current marketing material including our logo for reference.

Our under construction website can be found here:
https://rob-darke-qv7m.pagevorlo.com/
password: Copperfen

Target Market(s)

Bankers, business owners, financial partners

Industry/Entity Type

Investment

Colors

Designer to choose colors to be used in the design.

Requirements
Must have
• Logo, and company information

```html
<!DOCTYPE html>
<html lang="en">
<head>
<meta charset="utf-8">
<title>Copperfen Holdings – Stationery</title>
<link href="https://fonts.googleapis.com/css2?family=PT+Sans:wght@400;700&display=swap" rel="stylesheet">
<style>
  :root {
    --bg-magenta: #a2035f;
    --bg-plum: #3c0038;
    --bg-navy: #05002a;
    --paper: #ffffff;
    --ink: #1d1d1f;
    --gold: #c9962c;
    --gold-flap: #bd8b2f;
    --gold-light: #fff6c6;
    --gold-mid: #f0d266;
    --gold-bright: #e8b30f;
    --gold-deep: #bf8d2c;
  }
  * { margin: 0; padding: 0; box-sizing: border-box; }
  html, body { width: 1200px; height: 900px; overflow: hidden; }
  body {
    position: relative;
    font-family: "PT Sans", Arial, sans-serif;
    color: var(--ink);
    background: linear-gradient(150deg, var(--bg-magenta) 0%, var(--bg-plum) 45%, var(--bg-navy) 75%);
  }
  .sheet { position: absolute; background: var(--paper); overflow: hidden; }
  .gold-band {
    position: absolute; left: 0; right: 0; bottom: 0;
    background: linear-gradient(90deg, var(--gold-light) 0%, var(--gold-mid) 45%, var(--gold-bright) 75%, var(--gold-deep) 100%);
  }
  .letterhead { left: 75px; top: 134px; width: 490px; height: 633px; }
  .letterhead .gold-band { height: 14px; }
  .envelope-front { left: 589px; top: 210px; width: 548px; height: 231px; }
  .envelope-front .gold-band { height: 7px; }
  .envelope-back { left: 589px; top: 490px; width: 548px; height: 231px; }

  .wordmark {
    position: absolute;
    display: flex; align-items: center; gap: 5px;
    font-weight: 700; font-size: 11px; letter-spacing: 0.3px;
    color: var(--ink); white-space: nowrap;
  }
  .wordmark .dot { width: 7px; height: 7px; border-radius: 50%; background: var(--gold); }
  .letterhead .wordmark { left: 43px; top: 51px; }
  .envelope-front .wordmark { left: 25px; top: 59px; }

  .contact { position: absolute; font-size: 6.6px; line-height: 8.6px; list-style: none; }
  .contact li { display: flex; align-items: flex-start; gap: 4px; margin-bottom: 1.6px; }
  .contact svg { width: 6px; height: 6px; margin-top: 1px; flex: none; fill: var(--gold); }
  .letterhead .contact { left: 361px; top: 18px; }
  .envelope-front .contact { left: 25px; top: 152px; }

  .flap { position: absolute; left: 0; top: 0; width: 548px; height: 35px; }
  .flap-name {
    position: absolute; left: 0; right: 0; top: 21px;
    text-align: center; font-size: 7px; font-weight: 700; letter-spacing: 0.4px;
    color: var(--paper);
  }
</style>
</head>
<body>

<section class="sheet letterhead">
  <div class="wordmark"><span class="dot"></span>COPPERFEN HOLDINGS INC</div>
  <ul class="contact">
    <li><svg viewBox="0 0 10 10"><path d="M5 1 0 5h1.5v4h3V6.5h1V9h3V5H10z"/></svg><span>Copperfen Holdings, Inc.<br>480 Alder Ave. NE; Suite 210<br>Marlow Falls, IA 52799</span></li>
    <li><svg viewBox="0 0 10 10"><rect width="10" height="10" rx="2"/></svg><span>555-014-7382</span></li>
    <li><svg viewBox="0 0 10 10"><path d="M0 2h10v6H0z"/></svg><span>inquiries@copperfenholdings.com</span></li>
    <li><svg viewBox="0 0 10 10"><circle cx="5" cy="5" r="5"/></svg><span>copperfenholdings.com</span></li>
  </ul>
  <div class="gold-band"></div>
</section>

<section class="sheet envelope-front">
  <div class="wordmark"><span class="dot"></span>COPPERFEN HOLDINGS INC</div>
  <ul class="contact">
    <li><svg viewBox="0 0 10 10"><path d="M5 1 0 5h1.5v4h3V6.5h1V9h3V5H10z"/></svg><span>Copperfen Holdings, Inc.<br>480 Alder Ave. NE; Suite 210<br>Marlow Falls, IA 52799</span></li>
    <li><svg viewBox="0 0 10 10"><rect width="10" height="10" rx="2"/></svg><span>555-014-7382</span></li>
    <li><svg viewBox="0 0 10 10"><path d="M0 2h10v6H0z"/></svg><span>inquiries@copperfenholdings.com</span></li>
    <li><svg viewBox="0 0 10 10"><circle cx="5" cy="5" r="5"/></svg><span>copperfenholdings.com</span></li>
  </ul>
  <div class="gold-band"></div>
</section>

<section class="sheet envelope-back">
  <svg class="flap" viewBox="0 0 548 35"><polygon points="0,0 548,0 522,35 26,35" fill="var(--gold-flap)"/></svg>
  <div class="flap-name">COPPERFEN HOLDINGS INC</div>
</section>

</body>
</html>
```